The Brightwater Compass Business Card

We need an attractive business card with the logo that we bought from ArtVantly last year.
Our mission is to contribute to change the way today's leaders manage business companies bringing value to the workplace and helping them to build a new model of creating wealth.
Our logo is clear about our values : we seek Positive Change through People and are convinced that the pursuit of individual well-being and the chase of economic results can converge with the right management.
Management Consulting
Corinne Fabrelle
+34 612 98 70 31
corinne.fabrelle@thebrightwatercompass-mail.net
www.thebrightwatercompass-mail.net

```html
<!DOCTYPE html>
<html lang="en">
<head>
<meta charset="utf-8">
<title>The Brightwater Compass – Business Card</title>
<link rel="stylesheet" href="https://fonts.googleapis.com/css2?family=Cinzel:wght@400;500&family=Open+Sans:wght@400&display=swap">
<style>
  :root {
    --bg: #e4e5e7;
    --card: #ffffff;
    --teal: #138a89;
    --teal-soft: #9fd6d4;
    --ink: #3a3a3a;
    --shadow: rgba(0, 0, 0, 0.12);
  }
  * { margin: 0; padding: 0; box-sizing: border-box; }
  html, body {
    width: 1200px; height: 1200px; overflow: hidden;
    background: var(--bg);
  }
  .canvas {
    width: 1200px; height: 1200px;
    display: flex; flex-direction: column; align-items: center; justify-content: center;
    gap: 60px;
  }
  .card {
    position: relative;
    width: 860px; height: 492px;
    background: var(--card);
    box-shadow: 0 6px 24px var(--shadow);
    overflow: hidden;
  }
  .brand {
    display: flex; flex-direction: column; align-items: center;
    color: var(--teal);
    font-family: "Cinzel", serif; font-weight: 500;
  }
  .brand-mark {
    width: 22px; height: 22px; border-radius: 50%;
    background: var(--teal); margin-bottom: 14px;
  }
  .brand-name { letter-spacing: 1px; text-align: center; line-height: 1.15; }

  /* Contact side */
  .card--contact .brand { position: absolute; top: 48px; left: 80px; }
  .card--contact .brand-mark { width: 16px; height: 16px; margin-bottom: 10px; }
  .card--contact .brand-name { font-size: 28px; }
  .holder-name {
    position: absolute; top: 160px; left: 80px;
    font-family: "Cinzel", serif; font-weight: 400;
    font-size: 36px; letter-spacing: 2px; color: var(--teal);
  }
  .contact-list {
    position: absolute; top: 232px; left: 80px;
    list-style: none;
    font-family: "Open Sans", sans-serif; font-size: 19px; color: var(--ink);
  }
  .contact-list li { display: flex; align-items: center; gap: 14px; margin-bottom: 16px; }
  .contact-list svg { width: 20px; height: 20px; fill: var(--teal); flex: none; }
  .accent-rule {
    position: absolute; left: 0; right: 0; bottom: 76px;
    height: 2px; background: var(--teal);
  }
  .accent-band {
    position: absolute; left: 0; right: 0; bottom: 0;
    height: 64px; background: var(--teal);
  }
  .faint-mark {
    position: absolute; right: 40px; bottom: 56px;
    width: 170px; height: 170px; border-radius: 50%;
    background: var(--teal-soft); opacity: 0.6;
  }

  /* Logo side */
  .card--logo { display: flex; align-items: center; justify-content: center; }
  .card--logo .brand-name { font-size: 44px; }
</style>
</head>
<body>
<main class="canvas">
  <section class="card card--contact" aria-label="Business card, contact side">
    <div class="brand">
      <span class="brand-mark" aria-hidden="true"></span>
      <span class="brand-name">The Brightwater Compass</span>
    </div>
    <h1 class="holder-name">CORINNE FABRELLE</h1>
    <ul class="contact-list">
      <li>
        <svg viewBox="0 0 24 24" aria-hidden="true"><path d="M6.6 10.8a15.5 15.5 0 0 0 6.6 6.6l2.2-2.2a1 1 0 0 1 1-.25 11.4 11.4 0 0 0 3.6.57 1 1 0 0 1 1 1V20a1 1 0 0 1-1 1A17 17 0 0 1 3 4a1 1 0 0 1 1-1h3.5a1 1 0 0 1 1 1c0 1.25.2 2.45.57 3.6a1 1 0 0 1-.25 1z"/></svg>
        +34 612 98 70 31
      </li>
      <li>
        <svg viewBox="0 0 24 24" aria-hidden="true"><path d="M12 2a10 10 0 1 0 0 20 10 10 0 0 0 0-20zm6.9 6h-2.9a15.7 15.7 0 0 0-1.4-3.6A8 8 0 0 1 18.9 8zM12 4c.8 1.2 1.5 2.5 1.9 4h-3.8c.4-1.5 1.1-2.8 1.9-4zM4.3 14a8 8 0 0 1 0-4h3.4a16 16 0 0 0 0 4zm.8 2h2.9c.3 1.3.8 2.5 1.4 3.6A8 8 0 0 1 5.1 16zM8 8H5.1a8 8 0 0 1 4.3-3.6C8.8 5.5 8.3 6.7 8 8zm4 12c-.8-1.2-1.5-2.5-1.9-4h3.8c-.4 1.5-1.1 2.8-1.9 4zm2.3-6H9.7a14.6 14.6 0 0 1 0-4h4.6a14.6 14.6 0 0 1 0 4zm.3 5.6c.6-1.1 1.1-2.3 1.4-3.6h2.9a8 8 0 0 1-4.3 3.6zm1.7-5.6a16 16 0 0 0 0-4h3.4a8 8 0 0 1 0 4z"/></svg>
        www.thebrightwatercompass-mail.net
      </li>
      <li>
        <svg viewBox="0 0 24 24" aria-hidden="true"><path d="M2 5h20v14H2zm2 2v.5l8 5 8-5V7l-8 5z"/></svg>
        corinne.fabrelle@thebrightwatercompass-mail.net
      </li>
    </ul>
    <div class="faint-mark" aria-hidden="true"></div>
    <div class="accent-rule"></div>
    <div class="accent-band"></div>
  </section>

  <section class="card card--logo" aria-label="Business card, logo side">
    <div class="brand">
      <span class="brand-mark" aria-hidden="true"></span>
      <span class="brand-name">The Brightwater Compass</span>
    </div>
  </section>
</main>
</body>
</html>
```